Custom Wine Label for Restaurant

Our restaurant needs to create a custom wine label to place on wine bottles. I would like the wine to be called "Gerald's Cask Dark" and have our logo and the sketch of him or a new one on the front. There are some mandatory legal items that must be on the label: The mandatory items for the KPF are ABV (13.5%), the government warning, the vinted and bottled by section with our location and website. I have included a sample label. I would like a front and back. The back can be lorem ipsum filler text for the time being. This should be a white label with the red logos/fonts used. I have also uploaded the sample labels to base the size and legal stuff off, they are under "Boston"
Restaurant, Bar, Wine
- Like the ones on the logos

```html
<!DOCTYPE html>
<html lang="en">
<head>
<meta charset="utf-8">
<title>Gerald's Cask Dark – Wine Labels</title>
<link rel="stylesheet" href="https://fonts.googleapis.com/css2?family=Playfair+Display:wght@400;600&family=Montserrat:wght@400&family=Oswald:wght@400;500;600&display=swap">
<style>
  :root {
    --wine: #5a1219;
    --wine-bright: #7a1a28;
    --ink: #1a1a1a;
    --body-text: #3a3a3a;
    --paper: #ffffff;
    --stage: #ffffff;
    --art-grey: #c9c6c2;
    --art-gold: #e2b64a;
  }
  * { margin: 0; padding: 0; box-sizing: border-box; }
  html, body {
    width: 1200px; height: 1200px; overflow: hidden;
    background: var(--stage);
  }
  .sheet { position: relative; width: 1200px; height: 1200px; }

  .label {
    position: absolute;
    background: var(--paper);
    box-shadow: 6px 10px 12px rgba(0,0,0,0.28);
  }

  /* Front label */
  .label--front { left: 68px; top: 68px; width: 466px; height: 459px; }
  .front__name {
    position: absolute; left: 0; right: 0; top: 38px;
    text-align: center;
    font-family: "Playfair Display", serif; font-weight: 600;
    font-size: 70px; line-height: 1; color: var(--wine);
  }
  .front__variety {
    position: absolute; left: 0; right: 0; top: 144px;
    text-align: center;
    font-family: "Playfair Display", serif; font-weight: 600;
    font-size: 22px; letter-spacing: 0.5px; color: var(--wine);
  }
  .front__portrait {
    position: absolute; left: 35px; top: 182px; width: 400px; height: 250px;
    background:
      radial-gradient(ellipse at 52% 40%, rgba(226,182,74,0.85) 0%, rgba(226,182,74,0.35) 35%, rgba(255,255,255,0) 65%),
      radial-gradient(ellipse at 20% 80%, rgba(226,182,74,0.7) 0%, rgba(255,255,255,0) 50%),
      radial-gradient(ellipse at 50% 50%, var(--art-grey) 0%, rgba(201,198,194,0.6) 55%, rgba(255,255,255,0) 80%);
  }
  .front__brand {
    position: absolute; right: 22px; bottom: 42px;
    font-family: "Playfair Display", serif; font-weight: 600;
    font-size: 13px; line-height: 1.15; color: var(--wine); text-align: right;
  }

  /* Back label */
  .label--back { left: 816px; top: 142px; width: 363px; height: 357px; }
  .back__name {
    position: absolute; left: 0; right: 0; top: 26px;
    text-align: center;
    font-family: "Playfair Display", serif; font-weight: 600;
    font-size: 34px; line-height: 1; color: var(--wine);
  }
  .back__variety {
    position: absolute; left: 0; right: 0; top: 73px;
    text-align: center;
    font-family: "Playfair Display", serif; font-weight: 600;
    font-size: 10px; color: var(--wine);
  }
  .back__story {
    position: absolute; left: 20px; top: 100px; width: 323px;
    font-family: "Montserrat", sans-serif; font-size: 10.4px; line-height: 13.8px;
    color: var(--body-text);
    text-align: justify; text-align-last: center;
  }
  .back__brand {
    position: absolute; left: 46px; top: 246px;
    font-family: "Playfair Display", serif; font-weight: 600;
    font-size: 10px; line-height: 1.15; color: var(--wine);
  }
  .bottler {
    position: absolute; left: 175px; top: 248px; width: 162px; height: 26px;
    border: 1px solid var(--ink); border-radius: 3px;
    font-family: "Oswald", sans-serif; text-align: center; color: var(--ink);
  }
  .bottler__title {
    position: absolute; left: 50%; top: -7px; transform: translateX(-50%);
    background: var(--paper); padding: 0 2px;
    font-size: 8px; font-weight: 500; letter-spacing: 0.4px; white-space: nowrap; line-height: 12px;
  }
  .bottler__address {
    position: absolute; left: 0; right: 0; top: 6px;
    font-size: 7.5px; line-height: 10px; letter-spacing: 0.3px;
  }
  .bottler__site {
    position: absolute; left: 50%; top: 18px; transform: translateX(-50%);
    background: var(--paper); padding: 0 3px;
    font-size: 7.5px; line-height: 11px; color: var(--wine-bright); font-weight: 500; white-space: nowrap;
  }
  .back__content {
    position: absolute; right: 21px; top: 287px;
    font-family: "Oswald", sans-serif; font-weight: 600; font-size: 8.6px;
    letter-spacing: 0.2px; color: var(--ink);
  }
  .back__warning {
    position: absolute; left: 18px; top: 304px; width: 332px;
    font-family: "Oswald", sans-serif; font-weight: 500; font-size: 7.4px; line-height: 10px;
    color: var(--ink); text-transform: uppercase;
  }
  .back__warning strong { font-weight: 600; }
</style>
</head>
<body>
<main class="sheet">

  <section class="label label--front" aria-label="Front label">
    <h1 class="front__name">Gerald's</h1>
    <p class="front__variety">CASK DARK</p>
    <div class="front__portrait" role="img" aria-label="Sketch-style portrait of Gerald and Marion in grey pencil with a warm golden wash"></div>
    <p class="front__brand">Gerald &amp;<br>Marion's</p>
  </section>

  <section class="label label--back" aria-label="Back label">
    <h2 class="back__name">Gerald's</h2>
    <p class="back__variety">CASK DARK</p>
    <p class="back__story">Lorem ipsum dolor sit amet, consectetur adipisci elit, sed do eiusmod tempor incidunt ut labore et dolore magna aliqua. Ut enim ad minim veniam, quis nostrum exercitationem ullamco laboriosam, nisi ut aliquid ex ea commodi consequatur. Duis aute irure reprehenderit in voluptate velit esse cillum dolore eu fugiat nulla pariatur. Excepteur sint obcaecat cupiditat non proident, sunt in culpa qui officia deserunt mollit anim id est laborum.</p>
    <p class="back__brand">Gerald &amp;<br>Marion's</p>
    <div class="bottler">
      <span class="bottler__title">VINTED &amp; BOTTLED BY</span>
      <span class="bottler__address">GERALD &amp; MARION'S XXXXXXXXX</span>
      <span class="bottler__site">Gerald &amp; Marion's</span>
    </div>
    <p class="back__content">CONTAINS SULFITES: ALC. 13,5%, BY VOL. 750ml</p>
    <p class="back__warning"><strong>Government warning:</strong> (1) According to the Surgeon General, women should not drink alcoholic beverages during pregnancy because of the risk of birth defects.<br>(2) Consumption of alcoholic beverages impairs your ability to drive a car or operate machinery, and may cause health problems.</p>
  </section>

</main>
</body>
</html>
```